BrightPath Dental
Web Presence
BrightPath Dental - Information Technology
Creative Brief
Information Technology
www.brightpathdental-demo.com
Brightpath Dental provides a wide variety of high tech dental solutions at a competitive price. We pride ourselves on the extremely high level and speed of service that we provide to our clientele. We are a local computer company that specializes in bringing our clientele the best dental technology solutions available. By allowing us to correctly integrate the right dental technology solutions, it gives your practice a technological competitive edge, increases production, and significantly enhances your patient’s experience. We provide a full array of computer services for both small and large practices. Our team services PC's and networks, digital x-ray / imaging equipment, we also provide software & hardware sales, service, upgrades, and installations, as well as data storage and backup solutions. We also provide ongoing technical support to keep you comfortable with changing technologies and ensure your practice productivity.
would like CMS designed website for either joomla or wordpress. We need the wording and the design -- we are a Lumoverde Reseller and Installer so please check out their site listed below. our logo is available: http://orders.markcraftstudio-demo.com/contests/business-logo-brightpathdental
left side
http://www.lumoverdedental-demo.com/us_region/index.aspx
http://www.qwbadvisors-demo.com/articles
http://www.orb-sys-demo.com/index.html
Additional Sites that do similar work: http://www.mnzerodental-demo.com/dataprotection.htm http://www.fenwro-demo.com/customer_care.html http://www.glimvo-demo.com/ http://www.mnzerodental-demo.com/dataprotection.htm

```html
<!DOCTYPE html>
<html lang="en">
<head>
<meta charset="utf-8">
<title>BrightPath Dental – Customer Care</title>
<link rel="stylesheet" href="https://fonts.googleapis.com/css2?family=Arimo:wght@400;700&display=swap">
<style>
  :root{
    --brand-blue:#1b5db0;
    --brand-blue-dark:#124a93;
    --frame-grey:#c9c9c9;
    --text-dark:#1a1a1a;
    --link-grey:#555555;
    --card-grey-top:#d2d2d2;
    --card-grey-bottom:#9d9d9d;
    --card-title:#eeeeee;
    --logo-red:#c8202f;
    --white:#ffffff;
  }
  *{margin:0;padding:0;box-sizing:border-box}
  html,body{width:1200px;height:912px;overflow:hidden;background:var(--white)}
  body{font-family:"Arimo",Arial,sans-serif;color:var(--text-dark);position:relative}

  .site-header{position:absolute;left:0;top:0;width:1200px;height:118px}
  .brand{position:absolute;left:192px;top:34px;display:flex;align-items:center;gap:10px}
  .brand-mark{width:30px;height:30px;border-radius:50%;background:var(--logo-red)}
  .brand-name{font-size:30px;font-weight:700;color:var(--logo-red);letter-spacing:-0.5px}
  .utility-links{position:absolute;left:734px;top:12px;font-size:19px;color:var(--link-grey);letter-spacing:0.5px;word-spacing:4px}
  .search{position:absolute;left:813px;top:60px;display:flex;align-items:center;gap:8px}
  .search label{font-size:17px;font-weight:700;color:var(--link-grey)}
  .search input{width:138px;height:27px;border:1px solid #8a8a8a;background:var(--white)}

  .page-frame{position:absolute;left:148px;top:122px;width:904px;height:790px;border:6px solid var(--frame-grey);border-bottom:none}

  .main-nav{position:absolute;left:148px;top:128px;width:197px;height:328px;background:var(--brand-blue);border-radius:0 0 0 34px;padding-top:14px}
  .main-nav ul{list-style:none;text-align:center}
  .main-nav li{font-size:18px;font-weight:700;color:var(--white);height:34.5px;line-height:34.5px;letter-spacing:0.3px}

  .hero-photo{position:absolute;left:345px;top:128px;width:468px;height:310px;
    background:linear-gradient(160deg,#cfd8e6 0%,#6f86b8 30%,#2f4f9a 55%,#203770 80%,#b9c2cf 100%)}

  .contact-card{position:absolute;left:823px;top:153px;width:219px;height:256px;border-radius:6px;
    background:linear-gradient(180deg,var(--card-grey-top),var(--card-grey-bottom));text-align:center;color:var(--white)}
  .contact-card h2{font-size:30px;font-weight:700;color:var(--card-title);margin-top:12px;text-shadow:0 1px 0 #a0a0a0}
  .contact-card .phone{font-size:32px;font-weight:700;color:#f2f2f2;margin-top:8px}
  .contact-card .hours{font-size:21px;font-weight:700;margin-top:48px;line-height:28px}

  .content{position:absolute;left:345px;top:466px;width:672px;font-size:15.6px;line-height:23.6px}
  .content p{margin-bottom:23.6px}
  .content strong{font-weight:700}

  .social{position:absolute;left:912px;top:825px;display:flex;gap:5px}
  .social span{width:22px;height:22px;border-radius:4px;background:#9aa6b8}
  .social span.wide{width:54px}

  .site-footer{position:absolute;left:148px;top:857px;width:904px;height:50px;background:var(--brand-blue);
    border-top:3px solid var(--brand-blue-dark);color:var(--white);font-size:11px;font-weight:700;text-align:center;line-height:47px}
</style>
</head>
<body>
  <header class="site-header">
    <div class="brand"><span class="brand-mark"></span><span class="brand-name">BrightPath Dental</span></div>
    <div class="utility-links">EMAIL&nbsp;|&nbsp;BLOG&nbsp;|&nbsp;NEWSLETTER</div>
    <form class="search"><label for="q">Search</label><input id="q" type="text"></form>
  </header>

  <div class="page-frame"></div>

  <nav class="main-nav">
    <ul>
      <li>HOME</li>
      <li>OUR GALLERY</li>
      <li>YOUR EXPERTS</li>
      <li>ABOUT US</li>
      <li>CUSTOMER CARE</li>
      <li>PARTNERS</li>
      <li>CONTACT US</li>
    </ul>
  </nav>

  <div class="hero-photo" role="img" aria-label="Photo of a modern dental imaging room with scanning equipment under blue lighting"></div>

  <aside class="contact-card">
    <h2>Contact Us</h2>
    <div class="phone">888-555-0142</div>
    <div class="hours">Monday&nbsp; - &nbsp;Friday<br>9 :00 am&nbsp; - &nbsp;6 :00 pm</div>
  </aside>

  <main class="content">
    <p>Our Customer Care Center team comes to the office everyday prepared and ready to keep our clients' practices running smoothing, seamlessly and stress-free.</p>
    <p>Our Customer Care representatives and on-site technicians are not your run-of-the-mill service reps. It is critical by Fenwro standards that our technicians achieve a high level of experience and training before even joining Fenwro. Each has undergone a rigorous selection process and invests the time and energy to become accredited in dental practice management software and diagnostic equipment. Once accreditation is complete, the technician works in tandem with senior technicians, assuring they are given the Fenwro seal of approval before administering to your network.</p>
    <p><strong>On-site Service</strong> - Our support team is committed to being responsive to you, if and when you need us. We work to expedite your requests and schedule service to be as unobtrusive to your patients and practice as possible. Hourly rate.</p>
  </main>

  <div class="social" aria-label="Social links"><span></span><span></span><span class="wide"></span></div>

  <footer class="site-footer">Copyright © 2010&nbsp; - &nbsp;All rights reserved.</footer>
</body>
</html>
```